Design a label for a new brand of Gin the UK called Velvet Whisker - featuring a cat

The gin is Velvet Whisker in Colour and owners of Velvet Whisker cats will be a target market - the bottle is very distinctive and lends itself to a square label.

The Marshmallow root used in the production will be a draw to customers. The bottle is flat with a large front face that lends itself to a striking design. There should be enough space around the label to show the blue gin in the bottle as this is a feature.

Target Market(s)

gin lovers who may also own a Velvet Whisker car - age group 30 - 60 primarily female

Font styles to use
Sans Serif
Script

Colors

Designer to choose colors to be used in the design.

Requirements
Must have
• The gin will be a Velvet Whisker colour so the label must standout or completment the gin in the bottle. Here is the bottle you are working with
• https://www.flaskhaven-supply.co.uk/Glass-bottles/700ml-clear-glass-bottle-Tevrin.html
• Must have 70cl and 40% abv
Nice to have
• The predominent botanical (other than juniper) is marshmallow root, this is quite a sweet gin. The reference to marshmallow root would be a nice to have.

```html
<!DOCTYPE html>
<html lang="en">
<head>
<meta charset="utf-8">
<title>Velvet Whisker Gin – Label</title>
<link href="https://fonts.googleapis.com/css2?family=Arimo:wght@400&display=swap" rel="stylesheet">
<style>
  :root {
    --page: #ffffff;
    --label-grey: #6e7d86;
    --band-dark: #2f2d2f;
    --gold-deep: #b9801f;
    --gold-light: #ebc874;
    --gold-text: #d9a947;
    --ink-dark: #2b2b2d;
    --cat-light: #e9eaea;
    --cat-shade: #9fa3a5;
  }
  html, body {
    margin: 0;
    padding: 0;
    width: 1199px;
    height: 1200px;
    overflow: hidden;
    background: var(--page);
  }
  .canvas {
    width: 1199px;
    height: 1200px;
    display: flex;
    align-items: center;
    justify-content: center;
  }
  .gin-label {
    width: 700px;
    height: 818px;
    display: block;
  }
  .label-face { fill: var(--label-grey); }
  .gold-ring { fill: none; stroke: url(#goldRing); stroke-width: 18; }
  .root-band { fill: var(--band-dark); }
  .product-name {
    font-family: "Arimo", Arial, sans-serif;
    font-size: 50px;
    fill: var(--gold-text);
  }
  .label-detail {
    font-family: "Arimo", Arial, sans-serif;
    fill: var(--ink-dark);
  }
  .volume { font-size: 19px; }
  .strength { font-size: 17px; }
  .strength-unit { font-size: 10px; }
</style>
</head>
<body>
<main class="canvas">
  <svg class="gin-label" viewBox="0 0 536 626" xmlns="http://www.w3.org/2000/svg">
    <defs>
      <linearGradient id="goldRing" x1="0" y1="0" x2="1" y2="1">
        <stop offset="0" stop-color="var(--gold-light)"/>
        <stop offset="0.5" stop-color="var(--gold-deep)"/>
        <stop offset="1" stop-color="var(--gold-light)"/>
      </linearGradient>
      <radialGradient id="catTone" cx="0.5" cy="0.45" r="0.6">
        <stop offset="0" stop-color="var(--cat-light)"/>
        <stop offset="1" stop-color="var(--cat-shade)"/>
      </radialGradient>
      <linearGradient id="rootTone" x1="0" y1="0" x2="0" y2="1">
        <stop offset="0" stop-color="var(--band-dark)" stop-opacity="0.9"/>
        <stop offset="1" stop-color="var(--band-dark)" stop-opacity="0.35"/>
      </linearGradient>
      <clipPath id="faceClip">
        <ellipse cx="268" cy="313" rx="252" ry="297"/>
      </clipPath>
    </defs>

    <ellipse class="label-face" cx="268" cy="313" rx="259" ry="304"/>

    <g clip-path="url(#faceClip)">
      <path class="root-band" d="M0,330 Q268,410 536,320 L536,345 Q268,465 0,360 Z"/>
    </g>

    <g class="cat-portrait" role="img" aria-label="Hand-drawn portrait of a Persian cat">
      <ellipse cx="263" cy="170" rx="72" ry="80" fill="url(#catTone)"/>
    </g>

    <text class="product-name" x="268" y="333" text-anchor="middle">Velvet Whisker</text>

    <g class="marshmallow-root" role="img" aria-label="Ink drawing of marshmallow root growing beneath the band">
      <path d="M255,408 L285,408 Q330,470 360,560 Q250,575 150,565 Q200,470 255,408 Z" fill="url(#rootTone)"/>
    </g>

    <text class="label-detail volume" x="72" y="451">70cl</text>
    <text class="label-detail strength" x="398" y="453">40% <tspan class="strength-unit">abv</tspan></text>

    <ellipse class="gold-ring" cx="268" cy="313" rx="259" ry="304"/>
  </svg>
</main>
</body>
</html>
```